Criação de Logo e Papelaria (6 itens) para Reabilitaçao Oral/Periodontia/Implantodontia com credenciamento em cirurgia guiada por computador.
" Profissional liberal: cirurgiao- dentista especialista em periodontia e implantodontia. "

```html
<!DOCTYPE html>
<html lang="pt-BR">
<head>
<meta charset="utf-8">
<title>Cartão de visita e agenda de consultas</title>
<link href="https://fonts.googleapis.com/css2?family=Varela+Round&display=swap" rel="stylesheet">
<style>
  :root{
    --bg:#e9e6e1;
    --card-front:#f4f5f6;
    --card-front-edge:#dfe2e5;
    --ink:#1c5a6d;
    --ink-soft:#6a8c97;
    --teal:#4ccac4;
    --teal-light:#6fd6d1;
    --navy:#124a60;
    --white:#ffffff;
    --slot-line:#1c5a6d;
  }
  *{box-sizing:border-box;margin:0;padding:0}
  html,body{width:1200px;height:1200px;overflow:hidden}
  body{background:var(--bg);font-family:"Varela Round",Arial,sans-serif;position:relative}

  .card{position:absolute;left:240px;width:720px;border-radius:26px;box-shadow:0 6px 18px rgba(0,0,0,.18)}

  /* front */
  .card-front{top:161px;height:422px;background:radial-gradient(circle at 62% 30%,#ffffff 0%,var(--card-front) 45%,var(--card-front-edge) 100%)}
  .brand{position:absolute;right:58px;top:30px;width:210px;text-align:center;color:var(--ink)}
  .brand-dot{display:block;margin:0 auto 10px;width:64px;height:64px;border-radius:50%;background:var(--teal-light)}
  .brand-name{font-size:22px;line-height:1.1}
  .brand-sub{font-size:11px;letter-spacing:2px;color:var(--ink-soft);margin-top:4px}
  .brand-reg{font-size:8px;letter-spacing:1px;color:var(--ink-soft);margin-top:2px}
  .contact{position:absolute;left:36px;top:150px;list-style:none;color:var(--ink);font-size:20.5px;line-height:31px}

  /* back */
  .card-back{top:636px;height:432px;background:var(--teal)}
  .back-title{position:absolute;left:0;right:0;top:12px;text-align:center;color:var(--white);font-size:30px;font-weight:normal;letter-spacing:1px}
  .schedule{position:absolute;left:36px;right:32px;top:58px;bottom:34px;background:var(--navy);border-radius:22px;padding:4px 20px 0}
  .schedule-grid{display:grid;grid-template-columns:132px 122px 132px 122px;justify-content:space-between;row-gap:15px}
  .col-head{color:var(--white);font-size:27px;text-align:center;height:38px;line-height:38px}
  .slot{height:43px;background:var(--white);border-radius:4px;color:var(--slot-line);font-size:22px;display:flex;align-items:center;justify-content:center}
  .slot-date{font-size:18px;letter-spacing:-1px;padding-top:8px}
  .slot-time{font-weight:bold}
</style>
</head>
<body>

<section class="card card-front" aria-label="Frente do cartão">
  <div class="brand">
    <span class="brand-dot"></span>
    <div class="brand-name">Dr. Rafael Montenar</div>
    <div class="brand-sub">Reabilitação Oral</div>
    <div class="brand-reg">CRO-RJ 00000</div>
  </div>
  <ul class="contact">
    <li>Vale do Sereno - RJ</li>
    <li>Rua das Acácias, 245 - sala 03 Centro.</li>
    <li>Tel: 22 2555 0148 Cep:28000-100</li>
    <li>Porto Aurora - RJ - Clínica Serena Medicina e Estética</li>
    <li>Rua Jorge Lessa, 410 - Bela Vista.</li>
    <li>Tel: 22 2555 0172/2555 0193</li>
    <li>Cep:27900-210</li>
    <li>email: contato@rmontenar.com.br</li>
  </ul>
</section>

<section class="card card-back" aria-label="Verso do cartão">
  <h2 class="back-title">Próximas consultas</h2>
  <div class="schedule">
    <div class="schedule-grid">
      <div class="col-head">data</div><div class="col-head">hora</div><div class="col-head">data</div><div class="col-head">hora</div>
      <div class="slot slot-date">____/____</div><div class="slot slot-time">:</div><div class="slot slot-date">____/____</div><div class="slot slot-time">:</div>
      <div class="slot slot-date">____/____</div><div class="slot slot-time">:</div><div class="slot slot-date">____/____</div><div class="slot slot-time">:</div>
      <div class="slot slot-date">____/____</div><div class="slot slot-time">:</div><div class="slot slot-date">____/____</div><div class="slot slot-time">:</div>
      <div class="slot slot-date">____/____</div><div class="slot slot-time">:</div><div class="slot slot-date">____/____</div><div class="slot slot-time">:</div>
      <div class="slot slot-date">____/____</div><div class="slot slot-time">:</div><div class="slot slot-date">____/____</div><div class="slot slot-time">:</div>
    </div>
  </div>
</section>

</body>
</html>
```